Business Card Design Project

We are looking for a new business card design for a Drilling company in WA, Australia.

We are in between offices, however require a design in the meantime due to some upcoming events with our basic information.

The Logo for our company is Blue and Grey and would like this colour scheme throughout.

We are quite a new company so would like a memorable design that stands out and communicates a strong commitment to safety, quality of work and performance.

The company name is Ironbark Boring Group (IBG)

The details to be included are as follows:

Gavin Thorley
Managing Director
m.0481639207
e.gavin@ibgpty.com.au

Martin Thorley
Director
m.0419852637
e.martin@ibgpty.com.au

Industry/Entity Type

Events

Requirements
Must have
• Under the Logo, we would like 'Western Australia'

```html
<!DOCTYPE html>
<html lang="en">
<head>
<meta charset="utf-8">
<title>Ironbark Boring Group – Business Card</title>
<link rel="stylesheet" href="https://fonts.googleapis.com/css2?family=Oswald:wght@600&family=Open+Sans:wght@400;600;700&display=swap">
<style>
  :root {
    --backdrop: #d8c3a2;
    --card-white: #ffffff;
    --card-grey: #77777b;
    --brand-blue: #1c3f86;
    --brand-grey: #7a7a7d;
    --text-grey: #555558;
    --rule-grey: #9a9a9d;
    --faint: #e6eaf0;
  }
  * { margin: 0; padding: 0; box-sizing: border-box; }
  html, body { width: 1200px; height: 444px; overflow: hidden; }
  body {
    background: var(--backdrop);
    position: relative;
    font-family: "Open Sans", Arial, sans-serif;
  }
  .card {
    position: absolute;
    overflow: hidden;
  }
  .card--front {
    left: 58px; top: 72px; width: 512px; height: 296px;
    background: var(--card-white);
  }
  .card--back {
    left: 617px; top: 74px; width: 525px; height: 300px;
    background: var(--card-grey);
  }

  .brand {
    position: absolute;
    display: flex;
    align-items: center;
    gap: 10px;
  }
  .brand__mark {
    width: 18px; height: 18px;
  }
  .brand__name {
    font-family: "Oswald", "Arial Narrow", sans-serif;
    font-weight: 600;
    text-transform: uppercase;
    line-height: 1;
    letter-spacing: 0.5px;
  }
  .front-brand { left: 48px; top: 46px; }
  .front-brand .brand__mark { background: var(--brand-blue); }
  .front-brand .brand__name { color: var(--brand-blue); font-size: 32px; }

  .region {
    position: absolute;
    font-family: "Open Sans", Arial, sans-serif;
    font-weight: 700;
    font-size: 9px;
    letter-spacing: 0.8px;
  }
  .front-region { left: 216px; top: 128px; color: var(--brand-blue); }

  .faint-name {
    position: absolute;
    left: 4px; top: 168px;
    font-family: "Oswald", "Arial Narrow", sans-serif;
    font-weight: 600;
    font-size: 44px;
    line-height: 40px;
    text-transform: uppercase;
    color: var(--faint);
  }

  .contact {
    position: absolute;
    left: 207px;
    width: 290px;
  }
  .contact--director { top: 182px; }
  .contact--managing { top: 236px; }
  .contact__name {
    font-weight: 600;
    font-size: 15px;
    color: var(--brand-blue);
    line-height: 18px;
  }
  .contact__role {
    font-size: 12.5px;
    color: var(--text-grey);
    line-height: 16px;
  }
  .contact__details {
    position: absolute;
    left: 130px; top: 2px;
    font-size: 12.5px;
    color: var(--text-grey);
    line-height: 21px;
  }
  .contact__line { display: flex; align-items: center; gap: 6px; }
  .contact__line svg { width: 10px; height: 12px; flex: none; }
  .divider {
    position: absolute;
    left: 207px; top: 225px;
    width: 288px; height: 2px;
    background: var(--rule-grey);
  }

  .back-brand { left: 0; right: 0; top: 126px; justify-content: center; }
  .back-brand .brand__mark { background: #ffffff; }
  .back-brand .brand__name { color: #ffffff; font-size: 30px; }
  .back-region { left: 0; right: 0; top: 172px; text-align: center; color: #ffffff; }
</style>
</head>
<body>
  <section class="card card--front" aria-label="Business card front">
    <div class="faint-name" aria-hidden="true">Ironbark<br>Boring<br>Group</div>

    <div class="brand front-brand">
      <span class="brand__mark"></span>
      <span class="brand__name">Ironbark Boring Group</span>
    </div>
    <div class="region front-region">Western Australia</div>

    <div class="contact contact--director">
      <div class="contact__name">Martin Thorley</div>
      <div class="contact__role">Director</div>
      <div class="contact__details">
        <div class="contact__line">
          <svg viewBox="0 0 10 12"><rect x="1.5" y="0" width="7" height="12" rx="1.5" fill="#1c3f86"/><rect x="3" y="2" width="4" height="4" fill="#fff"/></svg>
          041-985-2637
        </div>
        <div class="contact__line">
          <svg viewBox="0 0 10 12"><rect x="0" y="3" width="10" height="7" fill="#1c3f86"/><path d="M0 3 L5 7 L10 3" stroke="#fff" stroke-width="1" fill="none"/></svg>
          e.martin@ibgpty.com.au
        </div>
      </div>
    </div>

    <div class="divider"></div>

    <div class="contact contact--managing">
      <div class="contact__name">Gavin Thorley</div>
      <div class="contact__role">Managing Director</div>
      <div class="contact__details">
        <div class="contact__line">
          <svg viewBox="0 0 10 12"><rect x="1.5" y="0" width="7" height="12" rx="1.5" fill="#1c3f86"/><rect x="3" y="2" width="4" height="4" fill="#fff"/></svg>
          048-163-9207
        </div>
        <div class="contact__line">
          <svg viewBox="0 0 10 12"><rect x="0" y="3" width="10" height="7" fill="#1c3f86"/><path d="M0 3 L5 7 L10 3" stroke="#fff" stroke-width="1" fill="none"/></svg>
          gavin@ibgpty.com.au
        </div>
      </div>
    </div>
  </section>

  <section class="card card--back" aria-label="Business card back">
    <div class="brand back-brand">
      <span class="brand__mark"></span>
      <span class="brand__name">Ironbark Boring Group</span>
    </div>
    <div class="region back-region">Western Australia</div>
  </section>
</body>
</html>
```